Building company buisness cards

We are looking for a sharp modern new look for our business cards.We are a New Zealand based company that specialises in house and land packages.We have attached a photo of the current logo and would like to see if it can be improved somehow if needed.We are open to any colours but we have chosen Black and White at this stage. Feel free to change the font and make the logo smarter looking.Play with the colours and see what looks best.We want a card that looks so good know one will want to throw it away!

Target Market(s)

Building profesonals, home buyers

Industry/Entity Type

Building

Contact Information for Business Card

Garrick Thorne
0274392068
garrickt@homevista.co.nz

Font styles to use
Serif
Sans Serif

Colors

Designer to choose colors to be used in the design.

Requirements
Must have
• Just the logo on one side and details on the other
• Clean simple looking card
Nice to have
• Round corners and detail like raised or spot UV
• Something that stands out
Should not have
• To title needed, Director etc

```html
<!DOCTYPE html>
<html lang="en">
<head>
<meta charset="utf-8">
<title>HomeVista Business Card</title>
<link rel="stylesheet" href="https://fonts.googleapis.com/css2?family=Work+Sans:wght@400;500;600&display=swap">
<style>
  :root {
    --page-bg: #d9d2c8;
    --card-bg: #ece8e1;
    --card-edge: #f6f3ee;
    --ink: #1c1b1a;
    --ink-soft: #3a3836;
    --rule: #2a2927;
    --band: #121212;
  }
  html, body {
    margin: 0;
    padding: 0;
    width: 1200px;
    height: 1047px;
    overflow: hidden;
    background: var(--page-bg);
    font-family: "Work Sans", Arial, sans-serif;
    color: var(--ink);
  }
  .business-card {
    position: absolute;
    left: 150px;
    top: 291px;
    width: 948px;
    height: 513px;
    background: var(--card-bg);
    border: 1px solid var(--card-edge);
    border-radius: 22px;
    overflow: hidden;
    box-sizing: border-box;
  }
  .brand-name {
    position: absolute;
    left: 50px;
    top: 46px;
    margin: 0;
    font-size: 62px;
    font-weight: 600;
    letter-spacing: -1px;
    color: var(--ink-soft);
    line-height: 1;
  }
  .person-name {
    position: absolute;
    right: 50px;
    top: 238px;
    margin: 0;
    font-size: 30px;
    font-weight: 500;
    letter-spacing: 1.2px;
    text-transform: uppercase;
    line-height: 1.1;
  }
  .divider {
    position: absolute;
    left: 46px;
    right: 50px;
    top: 330px;
    height: 2px;
    background: var(--rule);
  }
  .contact-list {
    position: absolute;
    left: 46px;
    top: 362px;
    margin: 0;
    padding: 0;
    list-style: none;
    font-size: 21px;
    color: var(--ink-soft);
  }
  .contact-list li {
    display: flex;
    align-items: center;
    gap: 11px;
    height: 34px;
  }
  .contact-icon {
    width: 14px;
    height: 14px;
    flex: none;
  }
  .address {
    position: absolute;
    right: 50px;
    top: 396px;
    margin: 0;
    text-align: right;
    font-size: 21px;
    font-style: normal;
    line-height: 34px;
    color: var(--ink);
  }
  .card-band {
    position: absolute;
    left: 0;
    bottom: 0;
    width: 948px;
    height: 36px;
  }
</style>
</head>
<body>
  <section class="business-card">
    <p class="brand-name">HomeVista</p>

    <h1 class="person-name">Garrick Thorne</h1>

    <div class="divider"></div>

    <ul class="contact-list">
      <li>
        <svg class="contact-icon" viewBox="0 0 16 16" aria-hidden="true"><path d="M3.5 1.5l2.5 0 1 3.5-1.8 1.2a9 9 0 0 0 4.6 4.6l1.2-1.8 3.5 1v2.5c0 .8-.7 1.5-1.5 1.5C7 14 2 9 2 3c0-.8.7-1.5 1.5-1.5z" fill="#3a3836"/></svg>
        <span>0274392068</span>
      </li>
      <li>
        <svg class="contact-icon" viewBox="0 0 16 16" aria-hidden="true"><rect x="1.5" y="3.5" width="13" height="9" fill="none" stroke="#3a3836" stroke-width="1.6"/><path d="M1.5 3.5l6.5 5 6.5-5" fill="none" stroke="#3a3836" stroke-width="1.6"/></svg>
        <span>garrickt@homevista.co.nz</span>
      </li>
      <li>
        <svg class="contact-icon" viewBox="0 0 16 16" aria-hidden="true"><circle cx="8" cy="8" r="6.5" fill="none" stroke="#3a3836" stroke-width="1.4"/><ellipse cx="8" cy="8" rx="2.8" ry="6.5" fill="none" stroke="#3a3836" stroke-width="1.2"/><path d="M1.5 8h13M2.5 4.8h11M2.5 11.2h11" stroke="#3a3836" stroke-width="1.1"/></svg>
        <span>www.homevista.co.nz</span>
      </li>
    </ul>

    <address class="address">218b Larch Avenue,<br>Christchurch, NZ, 8014</address>

    <svg class="card-band" viewBox="0 0 948 36" aria-hidden="true">
      <path d="M0 8 H540 L550 13 H0 Z" fill="var(--band)"/>
      <path d="M0 24 H520 C545 24 560 2 590 2 H948 V36 H0 Z" fill="var(--band)"/>
    </svg>
  </section>
</body>
</html>
```